Charity website needing new website design

Hi there. We are looking to get a revamped website for our non for profit charity. We specialise in eye cataract surgeries and ear care around the world. Please visit our website brightcareaid.org.au for the current layout.
I have attached a brief with photos. The about us page please include an interactive map showing our locations we operate in. The website should be easy to use, match our logo design and be clear to navigate. Pixvault and other images can be used if they fit the scheme of the website and feel. The donation page should incorporate the gateway to receive donations. The team page should have each photo of the team member next to it. Please compare to other charity websites such as ORANTA, Global Haven etc. Another website which has a lovely and easy to use scheme is tkqhaustralia.org.au
The tabs should be in the following order:
About us, Why Health? Our Team, Eye Care Programs, Ear Care Programs, Contact Us, Donate.
Please make sure the website is both compatible with mobile & computer.
The Listed Benefactor Badge can be at the footer of the page with details of brightcare etc

```html
<!DOCTYPE html>
<html lang="en">
<head>
<meta charset="utf-8">
<title>BrightCare Aid Foundation</title>
<link href="https://fonts.googleapis.com/css2?family=Jost:wght@300;400;500;600;700&display=swap" rel="stylesheet">
<style>
:root{
  --green:#2eaa6e;
  --green-dark:#1f8f5b;
  --navy:#134b5f;
  --navy-deep:#0d3d52;
  --orange:#f5a733;
  --teal:#1380a4;
  --gold:#c9ae3e;
  --text:#4a4a4a;
  --grey-bg:#e9ecec;
}
*{box-sizing:border-box;margin:0;padding:0}
html,body{width:1200px;height:3588px;overflow:hidden}
body{font-family:"Jost",sans-serif;color:var(--text);background:#fff;position:relative}
.abs{position:absolute}
.stripe{position:absolute;left:0;width:1200px;height:4px;display:flex}
.stripe span{flex:1}
.stripe span:nth-child(1){background:var(--navy)}
.stripe span:nth-child(2){background:var(--green)}
.stripe span:nth-child(3){background:var(--orange)}
.stripe span:nth-child(4){background:var(--gold)}

/* header */
.site-header{position:absolute;left:0;width:1200px;background:#fff}
.brand{position:absolute;display:flex;align-items:center;gap:8px;font-weight:600;letter-spacing:.5px;line-height:15px;white-space:nowrap}
.brand i{display:block;border-radius:50%;flex:none}
.site-header .brand{left:96px;top:24px;color:var(--navy);font-size:15px}
.site-header .brand i{width:34px;height:34px;background:var(--green)}
.main-nav{position:absolute;left:330px;top:37px;display:flex;gap:24px;font-size:11.5px;font-weight:500;color:var(--navy-deep);text-transform:uppercase;white-space:nowrap}
.donate-btn{position:absolute;left:980px;top:22px;width:122px;height:44px;background:var(--green);color:#fff;border-radius:6px;font-weight:600;font-size:16px;display:flex;align-items:center;justify-content:center}

/* hero */
.hero{position:absolute;top:95px;left:0;width:1200px;height:514px;background:linear-gradient(90deg,#2eaa6e 0%,#3bb07a 38%,#8fc4a8 60%,#c4a58a 80%,#a2543a 100%)}
.hero-title{position:absolute;left:96px;top:105px;color:#fff;font-size:40px;line-height:49px;font-weight:600;letter-spacing:.5px}
.hero-text{position:absolute;left:96px;top:262px;width:490px;color:#fff;font-size:12.5px;line-height:21px;font-weight:300}
.btn-orange{position:absolute;left:95px;top:348px;width:161px;height:47px;background:var(--orange);color:#fff;border-radius:6px;font-weight:500;font-size:17px;display:flex;align-items:center;justify-content:center}

/* section labels */
.dot{position:absolute;width:30px;height:30px;border-radius:50%;background:var(--green);opacity:.85}
.kicker{position:absolute;font-size:18px;font-weight:300;color:#666}
.section-title{position:absolute;font-size:44px;font-weight:700;color:var(--navy);letter-spacing:1px;line-height:1}
.body-copy{position:absolute;font-size:14px;line-height:26px;font-weight:300;color:#555}
.btn-green{position:absolute;background:var(--green);color:#fff;border-radius:6px;font-weight:500;display:flex;align-items:center;justify-content:center}

/* services */
.price-circle{position:absolute;border-radius:50%;color:#fff;text-align:center;display:flex;flex-direction:column;justify-content:center;align-items:center}
.price-circle b{font-size:46px;font-weight:700;line-height:1}
.price-circle span{font-size:21px;font-weight:600;line-height:29px;margin-top:6px}

/* learn band */
.learn-band{position:absolute;top:1234px;left:0;width:1200px;height:438px;background:linear-gradient(90deg,#0f7296,#1386ac 55%,#1c8fb5)}
.learn-photo{position:absolute;left:596px;top:0;width:604px;height:438px;border-radius:320px 0 0 320px;background:linear-gradient(120deg,#c9a07a,#8a5a3e 45%,#e2622a 70%,#6a7a88)}
.learn-title{position:absolute;left:96px;top:174px;color:#fff;font-size:44px;font-weight:600;line-height:60px;letter-spacing:.5px}

/* coming soon */
.feature{position:absolute;width:240px;text-align:center}
.feature .ring{width:198px;height:198px;border-radius:50%;border:3px dotted #222;margin:0 auto;display:flex;align-items:center;justify-content:center}
.feature .core{width:172px;height:172px;border-radius:50%;display:flex;align-items:center;justify-content:center}
.feature h3{margin-top:30px;font-size:22px;font-weight:500;color:#111;line-height:28px;letter-spacing:.3px}

/* newsletter */
.newsletter{position:absolute;top:2900px;left:0;width:1200px;height:299px;background:linear-gradient(90deg,#e4e7e7,#d3d6d6 60%,#e8eaea)}
.field{position:absolute;background:#fff;border-radius:5px;font-size:15px;color:#666;padding:0 16px;display:flex;align-items:center;font-weight:300}

/* footer */
.footer-col{position:absolute;top:3296px}
.footer-col h4{font-size:24px;font-weight:600;color:#111;letter-spacing:.8px;margin-bottom:26px}
.footer-col li{list-style:none;font-size:19px;color:#666;line-height:34px;display:flex;gap:12px}
.footer-col li::before{content:"»";color:var(--green);width:14px}
.footer-col li.plain::before{content:""}
.footer-col li b{color:#111;font-weight:600}
.badge{position:absolute;left:1101px;top:3434px;width:72px;height:72px;border-radius:50%;border:3px solid #8fb7d4;background:#fff}
.bottom-bar{position:absolute;top:3510px;left:0;width:1200px;height:78px;background:var(--navy-deep)}
.bottom-bar .brand{left:76px;top:22px;color:#fff;font-size:16px;line-height:16px}
.bottom-bar .brand i{width:32px;height:32px;border:2px solid #fff}
.copyright{position:absolute;left:610px;top:29px;color:#fff;font-size:16px;font-weight:500}
</style>
</head>
<body>

<div class="stripe" style="top:0"><span></span><span></span><span></span><span></span></div>
<header class="site-header" style="top:4px;height:91px">
  <div class="brand"><i></i><span>BRIGHTCARE AID<br>FOUNDATION</span></div>
  <nav class="main-nav">
    <span>About Us</span><span>Why Health?</span><span>Our Team</span><span>Eye Care Programs</span><span>Ear Care Programs</span><span>Contact Us</span>
  </nav>
  <div class="donate-btn">DONATE</div>
</header>

<section class="hero">
  <div class="abs" role="img" aria-label="Photo of smiling children in a village" style="left:560px;top:0;width:640px;height:514px;background:linear-gradient(90deg,rgba(46,170,110,0),rgba(150,110,80,.25))"></div>
  <h1 class="hero-title">HELP BRING BASIC HEALTH<br>CARE TO EVERY PERSON ON<br>THE PLANET</h1>
  <p class="hero-text">Through symbiotic health programs brightcare aid foundation provides innovative solutions to Eye and Hearing Health in the developing world with an ethical professional and sustainable approach.</p>
  <div class="btn-orange">LEARN MORE</div>
</section>

<section class="services">
  <div class="abs" role="img" aria-label="Orange paint splash" style="left:92px;top:675px;width:478px;height:478px;border-radius:46% 54% 40% 60% / 55% 45% 55% 45%;background:var(--orange)"></div>
  <div class="price-circle" role="img" aria-label="Eye care patient photo tinted blue" style="left:327px;top:689px;width:212px;height:212px;background:radial-gradient(circle,#5aa9d0,#2a88bb)"><b>$10</b><span>EYE CARE</span></div>
  <div class="price-circle" role="img" aria-label="Ear care patient photo tinted navy" style="left:99px;top:788px;width:212px;height:212px;background:radial-gradient(circle,#2a6172,#164b5c)"><b>$25</b><span>EAR CARE</span></div>
  <div class="price-circle" role="img" aria-label="General health patient photo tinted green" style="left:292px;top:931px;width:212px;height:212px;background:radial-gradient(circle,#4cbb87,#2a9d68)"><b>$50</b><span>GENERAL<br>HEALTH</span></div>

  <div class="dot" style="left:627px;top:705px"></div>
  <div class="kicker" style="left:620px;top:758px">What We Do</div>
  <h2 class="section-title" style="left:619px;top:797px">OUR SERVICES</h2>
  <p class="body-copy" style="left:620px;top:870px;width:460px">Charities often focus on the last component of aid, which is at times critically required without focusing on the root cause of poverty. &nbsp;BrightCare Aid Foundation focuses on the fundamental factors of poverty through providing health programs such as preventable blindness operations and hearing loss restoration.</p>
  <div class="btn-green" style="left:620px;top:1030px;width:473px;height:53px;font-size:15px;font-weight:600">TÜRKIYE AND SYRIA EARTHQUAKE MEDICAL EMERGENCY AID</div>
</section>

<section class="learn-band">
  <div class="learn-photo" role="img" aria-label="Photo of a medic treating a patient on a clinic bed"></div>
  <div class="dot" style="left:108px;top:88px;background:#fff;opacity:.9"></div>
  <div class="kicker" style="left:99px;top:132px;color:#fff;font-size:18px">BrightCare gifting vision</div>
  <h2 class="learn-title">LEARN<br>ABOUT BRIGHTCARE<br>AID FOUNDATION.</h2>
</section>

<section class="about">
  <div class="abs" role="img" aria-label="Decorative tree illustration filled with photo collage" style="left:67px;top:1786px;width:494px;height:441px;border-radius:48% 52% 30% 30%;background:linear-gradient(135deg,#b9bcbf,#8a7060 40%,#d0d2d4 70%,#6f7478)"></div>
  <div class="dot" style="left:627px;top:1803px"></div>
  <div class="kicker" style="left:622px;top:1850px;color:var(--navy)">We brightcare a world with vision</div>
  <h2 class="section-title" style="left:622px;top:1894px">ABOUT US</h2>
  <p class="body-copy" style="left:618px;top:1965px;width:480px">With over 70 years of humanitarian aid experience across our members collectively. United in our passion we established brightcare aid foundation to provide innovative, sustainable, ethical and professional symbiotic solutions across health programs focussing on restorative eyesight and hearing procedures. We brightcare quality healthcare and improvement of general health and wellbeing coupled with treating and preventing other health conditions.</p>
  <div class="btn-green" style="left:620px;top:2152px;width:177px;height:58px;font-size:18px">LEARN MORE</div>
</section>

<section class="coming-soon">
  <div class="dot" style="left:585px;top:2345px"></div>
  <div class="kicker" style="left:0;width:1200px;text-align:center;top:2396px">Why Choose Us</div>
  <h2 class="section-title" style="left:0;width:1200px;text-align:center;top:2441px">COMING SOON</h2>

  <div class="feature" style="left:100px;top:2536px">
    <div class="ring"><div class="core" style="background:var(--navy)">
      <svg width="90" height="90" viewBox="0 0 90 90" fill="none" stroke="#fff" stroke-width="5" stroke-linejoin="round"><rect x="12" y="10" width="16" height="70" rx="5"/><path d="M38 30h34v50H38z"/><path d="M46 30V16h18v14"/><path d="M55 48c-6 8-6 16 0 16s6-8 0-16z"/></svg>
    </div></div>
    <h3>Health and Hygiene<br>Packs</h3>
  </div>
  <div class="feature" style="left:356px;top:2536px">
    <div class="ring"><div class="core" style="background:var(--green)">
      <svg width="90" height="90" viewBox="0 0 90 90" fill="none" stroke="#fff" stroke-width="5" stroke-linecap="round"><path d="M22 40c0-16 10-26 24-26s22 10 22 22c0 14-16 16-16 30 0 8-6 12-12 12s-10-4-10-8"/><path d="M34 40c0-8 5-12 12-12s10 4 10 10-8 8-8 14"/><path d="M76 30l8-6M78 45h9M76 60l8 6"/></svg>
    </div></div>
    <h3>Cataract and Hearing<br>Procedures</h3>
  </div>
  <div class="feature" style="left:612px;top:2536px">
    <div class="ring"><div class="core" style="background:var(--gold)">
      <svg width="90" height="90" viewBox="0 0 90 90" fill="none" stroke="#fff" stroke-width="4"><path d="M20 84V66c-8-6-12-14-12-24C8 24 24 10 42 10s32 14 32 30c0 6 4 12 8 16l-8 4v12H60v12"/><circle cx="42" cy="40" r="14"/><circle cx="42" cy="40" r="6"/></svg>
    </div></div>
    <h3>Health Education &amp;<br>Training</h3>
  </div>
  <div class="feature" style="left:868px;top:2536px">
    <div class="ring"><div class="core" style="background:var(--orange)">
      <svg width="90" height="90" viewBox="0 0 90 90" fill="none" stroke="#fff" stroke-width="4" stroke-linecap="round"><path d="M30 84V60l-6-10V38h10V30h10v8h10v-6h10v20c0 10-6 14-10 18v14z"/><path d="M45 6v10M20 14l6 8M70 14l-6 8M8 40h10M72 40h10"/></svg>
    </div></div>
    <h3>Strengthening Health<br>Systems</h3>
  </div>
</section>

<div class="stripe" style="top:2896px"><span></span><span></span><span></span><span></span></div>
<section class="newsletter">
  <div class="abs" role="img" aria-label="Soft greyscale close-up photo of an eye" style="left:600px;top:0;width:600px;height:299px;background:radial-gradient(ellipse at 60% 40%,#bfc3c3,rgba(230,232,232,0) 70%)"></div>
  <div class="dot" style="left:86px;top:58px"></div>
  <div class="kicker" style="left:76px;top:102px;font-size:20px;color:#555">Email</div>
  <h2 class="section-title" style="left:76px;top:136px;line-height:54px">SIGN UP TO<br>OUR NEWSLETTER</h2>
  <div class="field" style="left:569px;top:76px;width:248px;height:63px">Name</div>
  <div class="field" style="left:831px;top:76px;width:248px;height:63px">Email</div>
  <div class="field" style="left:569px;top:154px;width:248px;height:63px">Subject</div>
  <div class="btn-green" style="left:831px;top:154px;width:248px;height:63px;font-size:21px;font-weight:600">SUBMIT</div>
</section>
<div class="stripe" style="top:3197px"><span></span><span></span><span></span><span></span></div>

<footer>
  <div class="footer-col" style="left:97px">
    <h4>GET TO KNOW US</h4>
    <ul><li>About us</li><li>Coming soon</li></ul>
  </div>
  <div class="footer-col" style="left:462px">
    <h4>CONNECT</h4>
    <ul><li>E: info@brightcareaid.org.au</li><li>ABN: 42 713 205 916</li></ul>
  </div>
  <div class="footer-col" style="left:827px">
    <h4>BANK DETAILS</h4>
    <ul><li>Southern Harbour Bank</li><li>BSB:&nbsp;<b>064781</b></li><li class="plain">ACC:&nbsp;<b>318264059</b></li></ul>
  </div>
  <div class="badge" role="img" aria-label="Listed Benefactor Badge"></div>
  <div class="bottom-bar">
    <div class="brand"><i></i><span>BRIGHTCARE AID<br>FOUNDATION</span></div>
    <div class="copyright">2024 © Copyright, BrightCare Aid Foundation. All rights reserved.</div>
  </div>
</footer>

</body>
</html>
```